KLT Roofing Pty Ltd

We are a high end residential Roofing company
We would like something silimar to the attached logo with the same color scheme

Target Market(s)

High end residential Builders & Architects

Industry/Entity Type

Residential

```html
<!DOCTYPE html>
<html lang="en">
<head>
<meta charset="utf-8">
<title>KLT Roofing – Business Card</title>
<link rel="stylesheet" href="https://fonts.googleapis.com/css2?family=Roboto+Condensed:wght@300;400&display=swap">
<style>
  :root {
    --page-bg: #e9ebed;
    --card-dark: #3b4650;
    --card-mid: #4a5660;
    --card-light: #5d6973;
    --accent-blue: #1e9ad6;
    --text-white: #ffffff;
    --text-soft: #e4e8eb;
    --mark-faint: rgba(200, 208, 214, 0.55);
  }
  * { box-sizing: border-box; margin: 0; padding: 0; }
  html, body {
    width: 1200px;
    height: 1200px;
    overflow: hidden;
    background: var(--page-bg);
  }
  .canvas {
    width: 1200px;
    height: 1200px;
    display: flex;
    align-items: center;
    justify-content: center;
  }
  .business-card {
    position: relative;
    width: 1000px;
    height: 572px;
    background: radial-gradient(ellipse at 78% 8%, var(--card-light) 0%, var(--card-mid) 40%, var(--card-dark) 100%);
    box-shadow: 0 18px 40px rgba(0, 0, 0, 0.25);
    font-family: "Roboto Condensed", sans-serif;
    color: var(--text-white);
  }
  .brand-mark {
    position: absolute;
    left: 56px;
    top: 272px;
    width: 340px;
    display: flex;
    align-items: center;
    gap: 14px;
  }
  .brand-mark-square {
    width: 40px;
    height: 40px;
    flex: 0 0 40px;
    background: var(--mark-faint);
  }
  .brand-mark-name {
    font-weight: 400;
    font-size: 30px;
    line-height: 1;
    white-space: nowrap;
    color: var(--mark-faint);
  }
  .contact-block {
    position: absolute;
    left: 445px;
    top: 96px;
  }
  .person-name {
    font-weight: 400;
    font-size: 46px;
    line-height: 1.1;
    color: var(--text-white);
  }
  .person-role {
    font-weight: 300;
    font-size: 36px;
    line-height: 1.2;
    color: var(--accent-blue);
    margin-top: 4px;
  }
  .contact-list {
    list-style: none;
    margin-top: 52px;
  }
  .contact-item {
    display: flex;
    align-items: center;
    gap: 20px;
    font-weight: 300;
    font-size: 32px;
    color: var(--text-soft);
    height: 58px;
  }
  .contact-icon {
    width: 36px;
    height: 36px;
    flex: 0 0 36px;
    fill: var(--accent-blue);
  }
</style>
</head>
<body>
<main class="canvas">
  <article class="business-card">
    <div class="brand-mark">
      <span class="brand-mark-square"></span>
      <span class="brand-mark-name">KLT Roofing Pty Ltd</span>
    </div>

    <section class="contact-block">
      <h1 class="person-name">Corin Maddox</h1>
      <p class="person-role">General Manager</p>

      <ul class="contact-list">
        <li class="contact-item">
          <svg class="contact-icon" viewBox="0 0 24 24" aria-hidden="true">
            <path d="M12 1.5c-4.2 0-7.5 3.3-7.5 7.4 0 5.4 7.5 13.6 7.5 13.6s7.5-8.2 7.5-13.6c0-4.1-3.3-7.4-7.5-7.4zm0 10.3a3 3 0 1 1 0-6 3 3 0 0 1 0 6z"/>
          </svg>
          <span>218 Wexford Street, Eastvale</span>
        </li>
        <li class="contact-item">
          <svg class="contact-icon" viewBox="0 0 24 24" aria-hidden="true">
            <path d="M6.6 2.5l3 3.6c.4.5.4 1.2 0 1.7L8 9.6c1.1 2.4 3.9 5.4 6.4 6.6l1.8-1.6c.5-.4 1.2-.4 1.7 0l3.6 3c.5.4.6 1.2.1 1.7l-1.9 2.1c-.6.6-1.5.9-2.4.6C10.1 19.5 4.5 13.9 2 6.7c-.3-.9 0-1.8.6-2.4l2.1-1.9c.5-.5 1.3-.4 1.9.1z"/>
          </svg>
          <span>0400 555 218</span>
        </li>
        <li class="contact-item">
          <svg class="contact-icon" viewBox="0 0 24 24" aria-hidden="true">
            <path d="M2 5h20v2.2l-10 6.3L2 7.2z"/>
            <path d="M2 9.4l10 6.3 10-6.3V19H2z"/>
          </svg>
          <span>cmaddox@kltroofing.com.au</span>
        </li>
      </ul>
    </section>
  </article>
</main>
</body>
</html>
```